Business Card for staff member of football club FC Brenor

I would like to get a business card template for all staff member of our soccer club.

The card should use as much as possible the 2 colors of the club : Red which is the main color and blue which is the alternative color. It can be balanced between the two like our logo.

I prefer simple and lean design.

Contact Information for Business Card

Bussiness card should have all main stuff as describe here below in must have.

Font styles to use
Sans Serif

Requirements
Must have
• Name : Mathieu DERLAPIN
Fonction : Président
Mobile : +41 xx xxx xx xx
Email : first.lastname@fcbrenor.example
Adresse of the club : FC Brenor, 4820 Brenor
Website of the club : www.fcbrenor.example
Nice to have
• Version with and without picture of the staff member

A version for men, a version for women staff member.

```html
<!DOCTYPE html>
<html lang="fr">
<head>
<meta charset="utf-8">
<title>FC Brenor – Carte de visite</title>
<link rel="stylesheet" href="https://fonts.googleapis.com/css2?family=Cinzel:wght@400;600&family=Montserrat:wght@400;500;700;800&display=swap">
<style>
  :root {
    --club-red: #ec2336;
    --club-blue: #0a87cb;
    --paper: #ffffff;
    --ink: #4a4a4a;
    --backdrop: #e4e5e7;
  }
  * { box-sizing: border-box; margin: 0; padding: 0; }
  html, body { width: 1200px; height: 913px; overflow: hidden; }
  body {
    background: var(--backdrop);
    font-family: "Montserrat", sans-serif;
    display: flex;
    align-items: center;
    justify-content: center;
    gap: 40px;
  }
  .card {
    position: relative;
    width: 540px;
    height: 330px;
    border-radius: 18px;
    overflow: hidden;
    box-shadow: 0 10px 28px rgba(0,0,0,.18);
  }

  /* Front */
  .card-front { background: var(--club-blue); }
  .card-front .split { position: absolute; inset: 0; }
  .front-mark {
    position: absolute;
    inset: 0;
    display: flex;
    align-items: center;
    justify-content: center;
    gap: 14px;
  }
  .front-mark .dot {
    width: 34px; height: 34px; border-radius: 50%;
    background: var(--paper);
  }
  .front-mark .club-name {
    font-weight: 800;
    font-size: 46px;
    letter-spacing: 1px;
    color: var(--paper);
    text-transform: uppercase;
  }

  /* Back */
  .card-back { background: var(--paper); }
  .back-mark {
    position: absolute;
    left: 40px; top: 196px;
    display: flex; align-items: center; gap: 10px;
  }
  .back-mark .dot {
    width: 18px; height: 18px; border-radius: 50%;
    background: var(--club-red);
  }
  .back-mark .club-name {
    font-weight: 800;
    font-size: 24px;
    color: var(--club-red);
    text-transform: uppercase;
    white-space: nowrap;
  }
  .identity {
    position: absolute;
    right: 32px; top: 34px;
    text-align: right;
  }
  .identity .person {
    font-family: "Cinzel", serif;
    font-size: 26px;
    letter-spacing: 1px;
    white-space: nowrap;
  }
  .person .first { color: var(--club-red); font-weight: 400; }
  .person .last { color: var(--club-blue); font-weight: 600; }
  .identity .role {
    font-size: 13px;
    letter-spacing: 1.5px;
    color: var(--ink);
    margin-top: 2px;
  }

  .contacts {
    position: absolute;
    right: 22px; top: 150px;
    list-style: none;
    font-size: 11.5px;
    letter-spacing: .7px;
    color: var(--ink);
    text-transform: uppercase;
  }
  .contacts li {
    display: flex;
    justify-content: flex-end;
    align-items: center;
    gap: 10px;
    height: 23px;
    white-space: nowrap;
  }
  .contacts .icon {
    width: 14px; height: 14px;
    display: flex; align-items: center; justify-content: center;
    flex: none;
  }
  .contacts .tick { width: 2px; height: 12px; background: var(--club-red); }
  .contacts .ruled { border-right: 1.5px solid var(--club-blue); padding-right: 8px; margin-right: -9.5px; }
  .contacts .red { color: var(--club-red); }
  .contacts .blue { color: var(--club-blue); font-weight: 700; }

  .bottom-band {
    position: absolute;
    left: 0; right: 0; bottom: 0; height: 18px;
    background: linear-gradient(to right, var(--club-red) 0 70%, var(--club-blue) 70% 100%);
  }
  .band-knot {
    position: absolute;
    left: calc(70% - 11px); bottom: 4px;
    width: 22px; height: 22px; border-radius: 50%;
    background: var(--paper);
    border: 2px solid #222;
  }
</style>
</head>
<body>

  <section class="card card-front" aria-label="Recto de la carte">
    <svg class="split" viewBox="0 0 540 330" preserveAspectRatio="none" aria-hidden="true">
      <polygon points="0,0 245,0 330,330 0,330" fill="var(--club-red)"/>
      <line x1="245" y1="0" x2="330" y2="330" stroke="var(--paper)" stroke-width="6"/>
    </svg>
    <div class="front-mark">
      <span class="dot"></span>
      <span class="club-name">FC Brenor</span>
    </div>
  </section>

  <section class="card card-back" aria-label="Verso de la carte">
    <div class="back-mark">
      <span class="dot"></span>
      <span class="club-name">FC Brenor</span>
    </div>

    <header class="identity">
      <p class="person"><span class="first">MATHIEU</span> <span class="last">DERLAPIN</span></p>
      <p class="role">PRÉSIDENT</p>
    </header>

    <ul class="contacts">
      <li>
        <span><span class="red">FC</span> <span class="blue">BRENOR</span>, 4820 BRENOR</span>
        <span class="icon"><span class="tick"></span></span>
      </li>
      <li>
        <span>+41 XX XXX XX XX</span>
        <span class="icon ruled" aria-hidden="true"><svg width="14" height="14" viewBox="0 0 16 16"><path d="M4 2 L6 5 L5 6.5 C6 8.5 7.5 10 9.5 11 L11 10 L14 12 L12.5 14 C7 13.5 2.5 9 2 3.5 Z" fill="var(--club-red)"/></svg></span>
      </li>
      <li>
        <span><span class="red">MATHIEU@</span><span class="blue">FCBRENOR</span>.EXAMPLE</span>
        <span class="icon ruled" aria-hidden="true"><svg width="14" height="14" viewBox="0 0 16 16"><rect x="1.5" y="3.5" width="13" height="9" fill="var(--club-red)"/><path d="M1.5 3.5 L8 9 L14.5 3.5" stroke="#fff" stroke-width="1.2" fill="none"/></svg></span>
      </li>
      <li>
        <span>WWW.FCBRENOR.EXAMPLE</span>
        <span class="icon ruled" aria-hidden="true"><svg width="14" height="14" viewBox="0 0 16 16"><circle cx="8" cy="8" r="6.5" fill="var(--club-red)"/><path d="M1.5 8 H14.5 M8 1.5 C5 4.5 5 11.5 8 14.5 M8 1.5 C11 4.5 11 11.5 8 14.5" stroke="#fff" stroke-width="1" fill="none"/></svg></span>
      </li>
    </ul>

    <div class="bottom-band"></div>
    <span class="band-knot"></span>
  </section>

</body>
</html>
```